PawHush business card

Looking for a fun and cool biz card for a new company with patent pending products. I have products to help and protect dogs hearing. My colors are pantone blue and orange.
Updates

Please add tag line: Protect the ones you love...even your PawHushes!

Target Market(s)

Animal/Dog lovers!

Industry/Entity Type

Retail

Contact Information for Business Card

I'm looking for something simple yet fun with all the info included for biz cards

Colors
0555a3
f78f20

Requirements
Must have
• Logo
Nice to have
• name, website and email
Should not have
• phone number

```html
<!DOCTYPE html>
<html lang="en">
<head>
<meta charset="utf-8">
<title>PawHush Business Card</title>
<link rel="stylesheet" href="https://fonts.googleapis.com/css2?family=Open+Sans:wght@400;600;800&display=swap">
<style>
  :root {
    --backdrop: #ece8e2;
    --card-white: #ffffff;
    --brand-orange: #ff5000;
    --brand-blue: #0b2f8a;
    --ink: #3a3a3a;
    --tagline-ink: #ffffff;
    --card-shadow: 0 3px 8px rgba(0, 0, 0, 0.28);
  }
  * { box-sizing: border-box; margin: 0; padding: 0; }
  html, body {
    width: 1200px;
    height: 900px;
    overflow: hidden;
    background: var(--backdrop);
    font-family: "Open Sans", Arial, sans-serif;
  }
  .canvas { position: relative; width: 1200px; height: 900px; }

  .card {
    position: absolute;
    width: 580px;
    height: 357px;
    box-shadow: var(--card-shadow);
  }
  .card-front { left: 320px; top: 88px; background: var(--card-white); }
  .card-back { left: 320px; top: 478px; width: 583px; height: 358px; background: var(--brand-orange); }

  .wordmark {
    position: absolute;
    font-weight: 800;
    letter-spacing: -1px;
    line-height: 1;
    white-space: nowrap;
  }
  .card-front .wordmark {
    right: 32px;
    top: 46px;
    font-size: 66px;
    color: var(--brand-orange);
  }
  .card-back .wordmark {
    left: 0;
    right: 0;
    text-align: center;
    top: 138px;
    font-size: 86px;
    color: var(--brand-blue);
  }

  .tagline {
    position: absolute;
    left: 0;
    right: 0;
    top: 248px;
    text-align: center;
    font-size: 16px;
    font-weight: 600;
    color: var(--tagline-ink);
  }

  .holder { position: absolute; left: 37px; top: 168px; }
  .holder-name { font-size: 18px; font-weight: 600; line-height: 24px; }
  .holder-first { color: var(--brand-orange); }
  .holder-last { color: var(--brand-blue); }
  .holder-role { font-size: 15px; color: var(--ink); line-height: 22px; }

  .rule {
    position: absolute;
    left: 220px;
    top: 179px;
    width: 330px;
    height: 2px;
    background: var(--brand-orange);
  }

  .contact-list { position: absolute; left: 36px; top: 277px; list-style: none; }
  .contact-list li {
    display: flex;
    align-items: center;
    gap: 7px;
    font-size: 15px;
    line-height: 21px;
    color: var(--ink);
  }
  .contact-list svg { width: 13px; height: 13px; fill: var(--brand-orange); flex: none; }

  .address {
    position: absolute;
    right: 30px;
    top: 253px;
    text-align: right;
    font-size: 15px;
    line-height: 21px;
    color: var(--ink);
    font-style: normal;
  }
</style>
</head>
<body>
<main class="canvas">
  <section class="card card-front" aria-label="Business card front">
    <div class="wordmark">PawHush</div>

    <div class="holder">
      <p class="holder-name"><span class="holder-first">Daniel</span> <span class="holder-last">Reyes</span></p>
      <p class="holder-role">Managing Director</p>
    </div>
    <div class="rule"></div>

    <ul class="contact-list">
      <li>
        <svg viewBox="0 0 16 16" aria-hidden="true"><path d="M1 3h14v10H1zM2.5 4.5v.6L8 9l5.5-3.9v-.6z"/></svg>
        info@website.com
      </li>
      <li>
        <svg viewBox="0 0 16 16" aria-hidden="true"><path d="M8 1a7 7 0 1 0 0 14A7 7 0 0 0 8 1zm-2 3.5 3 1-1 2 3 1.5-1 3-3-1.5 1-2-3-1z"/></svg>
        www.website.com
      </li>
    </ul>

    <address class="address">
      1234, Address GoesHere<br>
      Country name, Code 12345
    </address>
  </section>

  <section class="card card-back" aria-label="Business card back">
    <div class="wordmark">PawHush</div>
    <p class="tagline">Protect the ones you love...even your PawHushes!</p>
  </section>
</main>
</body>
</html>
```